Flyer-Design für Lindauer Hotel
Zielgruppe
Lindauer Hotel
Aufgabenstellung
Texte: siehe alten Fyler,
drei Sterne dürfen nicht mehr in den Texten auftauchen.
www.lindauer-hotel-beispiel.de

```html
<!DOCTYPE html>
<html lang="de">
<head>
<meta charset="utf-8">
<title>Lindauer Hotel – Flyer</title>
<link href="https://fonts.googleapis.com/css2?family=Pinyon+Script&family=Roboto+Condensed:wght@300;400&display=swap" rel="stylesheet">
<style>
  :root{
    --gold:#a87d3c;
    --gold-dark:#8f6730;
    --text:#3b3733;
    --paper:#faf7f3;
    --paper-shade:#efe9e1;
  }
  html,body{margin:0;padding:0;overflow:hidden;}
  body{width:1200px;height:1200px;}
  .flyer{position:relative;width:1200px;height:1200px;overflow:hidden;
    background:radial-gradient(ellipse at 35% 55%, #ffffff 0%, var(--paper) 45%, var(--paper-shade) 100%);
    font-family:"Roboto Condensed",sans-serif;font-weight:300;color:var(--text);}
  .photo{position:absolute;}
  .photo--breakfast{left:0;top:0;width:600px;height:287px;
    background:linear-gradient(135deg,#d9c9b4 0%,#efe3d2 35%,#e8b878 60%,#d8553c 85%,#f2f0ea 100%);}
  .script{font-family:"Pinyon Script",cursive;color:var(--gold);font-weight:400;position:absolute;margin:0;white-space:nowrap;line-height:1;}
  .heading{font-size:36px;}
  .body-text{position:absolute;margin:0;font-size:18.5px;line-height:28px;}
  .intro{left:660px;top:124px;width:480px;line-height:24px;}
  .comfort-text{left:76px;top:440px;width:460px;}
  .sleep-text{left:76px;top:785px;width:460px;}
  .tile{position:absolute;width:215px;height:143px;}
  .tile--lounge{left:660px;top:247px;background:linear-gradient(160deg,#9db56f 0%,#e9e1d3 40%,#8a2f28 65%,#4a3e38 100%);}
  .tile--reception{left:922px;top:247px;background:linear-gradient(160deg,#b9c4cc 0%,#f1ece4 45%,#b03440 65%,#efe7da 100%);}
  .tile--buffet{left:660px;top:447px;background:linear-gradient(160deg,#e4e2de 0%,#b57a3a 45%,#6a2e26 75%,#d9c7a8 100%);}
  .tile--entrance{left:922px;top:447px;background:linear-gradient(160deg,#1f3553 0%,#33527c 45%,#c7d0dc 70%,#a83245 100%);}
  .caption{font-size:31px;}
  .amenities{position:absolute;margin:0;padding:0;list-style:none;font-size:18.5px;}
  .amenities li{position:relative;height:34px;line-height:34px;padding-left:29px;}
  .amenities li svg{position:absolute;left:0;top:10px;}
  .amenities li.plain{padding-left:29px;}
  .amenities--left{left:659px;top:725px;}
  .amenities--right{left:922px;top:725px;}
  .footer-wave{position:absolute;left:0;top:930px;}
</style>
</head>
<body>
<main class="flyer">
  <div class="photo photo--breakfast" role="img" aria-label="Frühstücksraum mit Buffet: Eier, Aufschnitt, Tomate-Mozzarella und Obst"></div>

  <h2 class="script heading" style="left:656px;top:54px;">Unterkunft:</h2>
  <p class="body-text intro">Nach einem reichhaltigen Frühstück starten Sie gut gestärkt in den Tag. Genau richtig, um einen Ausflug in die Umgebung zu unternehmen.</p>

  <div class="tile tile--lounge" role="img" aria-label="Lounge-Bereich mit Sesseln"></div>
  <div class="tile tile--reception" role="img" aria-label="Rezeption mit Treppe"></div>
  <div class="tile tile--buffet" role="img" aria-label="Frühstücksbuffet mit Marmeladen"></div>
  <div class="tile tile--entrance" role="img" aria-label="Eingangsbereich des Hotels an der Straße"></div>
  <span class="script caption" style="left:660px;top:368px;">Lounge-Bereich</span>
  <span class="script caption" style="left:923px;top:368px;">Rezeption</span>
  <span class="script caption" style="left:662px;top:568px;">Frühstücksbuffet</span>
  <span class="script caption" style="left:924px;top:568px;">Eingangsbereich</span>

  <h2 class="script heading" style="left:78px;top:326px;">Komfort und Tradition:</h2>
  <h2 class="script heading" style="left:147px;top:368px;">Lindauer Hotel Garni in Vechta</h2>
  <p class="body-text comfort-text">Als ruhiges Familien- und Nichtraucherhotel ist es bei seinen Gästen hoch geschätzt. Helle, freundlich gestaltete Zimmer und ein Service, der keine Wünsche offen lässt. Keine Frage, wer einen Aufenthalt in der altehrwürdigen Stadt Vechta plant, der wird sich von diesem Hotel begeistern können! Zentral gelegen bietet Lindauer Hotel in Vechta die ideale Ausgangsposition für Ausflüge in die nähere Umgebung.</p>

  <h2 class="script heading" style="left:78px;top:684px;">Finden Sie Ruhe und</h2>
  <h2 class="script heading" style="left:285px;top:718px;">Erholung im Schlaf!</h2>
  <p class="body-text sleep-text">Vechta bietet Geschäfts- und Erholungsreisenden eine Vielzahl an Möglichkeiten. Die dafür nötige Ruhe tanken Sie in Lindauer Hotel. Modern eingerichtete Einzel-, Doppel-, Dreibett-, Familienzimmer und Apartments mit Küche – allesamt mit Dusche/WC und kostenfreiem Zugang ins Internet (WLAN) und Nordlicht TV.</p>

  <h2 class="script heading" style="left:652px;top:668px;">weitere Annehmlichkeiten:</h2>

  <ul class="amenities amenities--left">
    <li><svg width="14" height="12" viewBox="0 0 14 12"><path d="M1 6 L5 10 L13 1" fill="none" stroke="var(--gold)" stroke-width="2.4"/></svg>kostenfreies WLAN</li>
    <li><svg width="14" height="12" viewBox="0 0 14 12"><path d="M1 6 L5 10 L13 1" fill="none" stroke="var(--gold)" stroke-width="2.4"/></svg>Private Parkplätze (4€ pro Tag)</li>
    <li><svg width="14" height="12" viewBox="0 0 14 12"><path d="M1 6 L5 10 L13 1" fill="none" stroke="var(--gold)" stroke-width="2.4"/></svg>Haustiere sind nicht gestattet</li>
    <li><svg width="14" height="12" viewBox="0 0 14 12"><path d="M1 6 L5 10 L13 1" fill="none" stroke="var(--gold)" stroke-width="2.4"/></svg>Minimarkt vor Ort</li>
    <li><svg width="14" height="12" viewBox="0 0 14 12"><path d="M1 6 L5 10 L13 1" fill="none" stroke="var(--gold)" stroke-width="2.4"/></svg>Snackautomat, Getränkeautomat</li>
    <li><svg width="14" height="12" viewBox="0 0 14 12"><path d="M1 6 L5 10 L13 1" fill="none" stroke="var(--gold)" stroke-width="2.4"/></svg>Nichtraucherzimmer</li>
    <li><svg width="14" height="12" viewBox="0 0 14 12"><path d="M1 6 L5 10 L13 1" fill="none" stroke="var(--gold)" stroke-width="2.4"/></svg>Aufzug</li>
    <li><svg width="14" height="12" viewBox="0 0 14 12"><path d="M1 6 L5 10 L13 1" fill="none" stroke="var(--gold)" stroke-width="2.4"/></svg>Heizung</li>
  </ul>
  <ul class="amenities amenities--right">
    <li><svg width="14" height="12" viewBox="0 0 14 12"><path d="M1 6 L5 10 L13 1" fill="none" stroke="var(--gold)" stroke-width="2.4"/></svg>Fahrradverleih</li>
    <li><svg width="14" height="12" viewBox="0 0 14 12"><path d="M1 6 L5 10 L13 1" fill="none" stroke="var(--gold)" stroke-width="2.4"/></svg>Golfplatz (max. 3 km entfernt)</li>
    <li><svg width="14" height="12" viewBox="0 0 14 12"><path d="M1 6 L5 10 L13 1" fill="none" stroke="var(--gold)" stroke-width="2.4"/></svg>Wandern</li>
    <li><svg width="14" height="12" viewBox="0 0 14 12"><path d="M1 6 L5 10 L13 1" fill="none" stroke="var(--gold)" stroke-width="2.4"/></svg>Radfahren</li>
    <li><svg width="14" height="12" viewBox="0 0 14 12"><path d="M1 6 L5 10 L13 1" fill="none" stroke="var(--gold)" stroke-width="2.4"/></svg>Express-Check-in/-out</li>
    <li><svg width="14" height="12" viewBox="0 0 14 12"><path d="M1 6 L5 10 L13 1" fill="none" stroke="var(--gold)" stroke-width="2.4"/></svg>Safe</li>
    <li><svg width="14" height="12" viewBox="0 0 14 12"><path d="M1 6 L5 10 L13 1" fill="none" stroke="var(--gold)" stroke-width="2.4"/></svg>Zeitungen</li>
    <li><svg width="14" height="12" viewBox="0 0 14 12"><path d="M1 6 L5 10 L13 1" fill="none" stroke="var(--gold)" stroke-width="2.4"/></svg>Schuhputzmaschine</li>
    <li class="plain">-service</li>
  </ul>

  <svg class="footer-wave" width="1200" height="270" viewBox="0 930 1200 270">
    <defs>
      <clipPath id="footer-area">
        <path d="M0 1065 C120 1020 240 985 370 985 C560 985 700 1100 880 1098 C1020 1096 1130 1060 1200 1025 L1200 1200 L0 1200 Z"/>
      </clipPath>
      <linearGradient id="room-a" x1="0" y1="0" x2="1" y2="1"><stop offset="0" stop-color="#e9e4dc"/><stop offset="1" stop-color="#c9c6c2"/></linearGradient>
      <linearGradient id="room-b" x1="0" y1="0" x2="1" y2="1"><stop offset="0" stop-color="#f1ebe0"/><stop offset=".6" stop-color="#b7453f"/><stop offset="1" stop-color="#c9a06a"/></linearGradient>
      <linearGradient id="room-c" x1="0" y1="0" x2="1" y2="1"><stop offset="0" stop-color="#f6f1ec"/><stop offset=".7" stop-color="#e6d9d3"/><stop offset="1" stop-color="#c9463d"/></linearGradient>
      <linearGradient id="room-d" x1="0" y1="0" x2="1" y2="1"><stop offset="0" stop-color="#2c3c55"/><stop offset=".6" stop-color="#9aa3ad"/><stop offset="1" stop-color="#6c6f73"/></linearGradient>
    </defs>
    <g clip-path="url(#footer-area)">
      <rect x="0" y="930" width="352" height="270" fill="url(#room-a)" role="img" aria-label="Einzelzimmer mit Bett und Leselampe"/>
      <rect x="352" y="930" width="356" height="270" fill="url(#room-b)" role="img" aria-label="Rezeption mit geschwungener Treppe"/>
      <rect x="708" y="930" width="358" height="270" fill="url(#room-c)" role="img" aria-label="Doppelzimmer mit rotem Teppich"/>
      <rect x="1066" y="930" width="134" height="270" fill="url(#room-d)" role="img" aria-label="Straßenansicht vor dem Hotel"/>
    </g>
    <path d="M0 1065 C120 1020 240 985 370 985 C560 985 700 1100 880 1098 C1020 1096 1130 1060 1200 1025 L1200 1010 C1130 1048 1020 1080 880 1082 C700 1084 560 967 370 967 C240 967 120 1000 0 1045 Z" fill="var(--gold)"/>
  </svg>
</main>
</body>
</html>
```